Specialized Personal Trainer Needs a Business Card Design

I need a business card design for my personal training business called Tall Pine Fitness. I have my Human Kinetics degree in Exercise Science from the Halvern Ridge College as well as an extra certification from NBKT (National Board of Kinetic Therapy). I work as a Cardiac Rehab Exercise Specialist and personal trainer giving specialized exercise prescriptions to those that have different heart conditions as well as work with the general population in weight loss, strength and conditioning, getting/staying fit.
Updates

I decided that I wanted a logo (as I did not have one before I submitted my project for a business card) so I am submitting a project to get a logo done and then I will decide on a business card, hopefully being able to use one of the designs already submitted.  My apologies for doing this backwards.  I am new to this so I appreciate your patience.

Thank you.

Hi, I have just created a project for a logo design (I realized I needed a logo and I should've done that first..oops!), please feel free to participate.  Once I receive a logo I like I will finalize my business card project and hopefully incorporate it into one of your business card designs. 

Thank you!

Target Market(s)

Business professionals

Industry/Entity Type

Personal Trainer

Requirements
Must have
• My name with my info:
Delia R. Whitcombe (BHK)
NBKT Certified Clinical Exercise Specialist & Personal Trainer
delia.whitcombe@tallpinefitness.example
Cell: 555-382-4170

Please make it double sided.
Nice to have
• An image that represents cardiac and general fitness training.

```html
<!DOCTYPE html>
<html lang="en">
<head>
<meta charset="utf-8">
<title>Tall Pine Fitness – Business Card</title>
<link rel="stylesheet" href="https://fonts.googleapis.com/css2?family=Jost:wght@400;600&display=swap">
<style>
  :root {
    --backdrop: #e4e2de;
    --card: #f6f6f4;
    --ink: #2a2a2a;
    --ink-soft: #3c3c3c;
    --accent: #d8262c;
  }
  * { box-sizing: border-box; margin: 0; padding: 0; }
  html, body {
    width: 1200px;
    height: 900px;
    overflow: hidden;
  }
  body {
    background: var(--backdrop);
    display: flex;
    align-items: center;
    justify-content: center;
    font-family: "Jost", "Century Gothic", sans-serif;
    color: var(--ink);
  }
  .business-card {
    position: relative;
    width: 460px;
    height: 805px;
    background: var(--card);
    box-shadow: 0 10px 30px rgba(0, 0, 0, 0.12);
  }
  .brand {
    position: absolute;
    top: 78px;
    right: 44px;
    display: flex;
    align-items: flex-start;
    gap: 18px;
  }
  .brand-square {
    width: 22px;
    height: 22px;
    background: var(--accent);
    margin-top: 14px;
  }
  .brand-name {
    font-weight: 400;
    font-size: 46px;
    line-height: 1.02;
    color: var(--ink);
    letter-spacing: 0.5px;
  }
  .identity {
    position: absolute;
    top: 318px;
    left: 40px;
    right: 36px;
  }
  .person-name {
    font-weight: 600;
    font-size: 26px;
    line-height: 1.2;
    color: var(--ink);
  }
  .person-title {
    font-weight: 400;
    font-size: 21px;
    line-height: 1.2;
    color: var(--ink-soft);
    margin-top: 2px;
  }
  .divider {
    position: absolute;
    top: 490px;
    left: 40px;
    right: 36px;
    border-top: 3px dotted var(--accent);
  }
  .contact {
    position: absolute;
    bottom: 120px;
    left: 30px;
    right: 36px;
    text-align: right;
    font-size: 18px;
    line-height: 1.55;
    color: var(--ink);
  }
  .contact-label {
    color: var(--accent);
    font-weight: 600;
  }
</style>
</head>
<body>
  <article class="business-card">
    <header class="brand">
      <span class="brand-square" aria-hidden="true"></span>
      <p class="brand-name">Tall<br>Pine<br>Fitness</p>
    </header>

    <section class="identity">
      <h1 class="person-name">Delia R. Whitcombe (BHK)</h1>
      <p class="person-title">NBKT Certified Clinical Exercise<br>Specialist &amp; Personal Trainer</p>
    </section>

    <hr class="divider">

    <section class="contact">
      <p class="contact-phone"><span class="contact-label">m</span>: 555-382-4170</p>
      <p class="contact-email"><span class="contact-label">e</span>: delia.whitcombe@tallpinefitness.example</p>
    </section>
  </article>
</body>
</html>
```